Letterhead Design Project

Quillfern Consulting is a newly created boutique consultancy focussing on delivering strategic consulting to medium and large businesses, with a focus on:
- Strategic planning and execution.
- Corporate function optimisation, especially in the areas of finance, commercial, and IT. This includes implementing the right functional design for the needs of the business, and ensuring the right skills.
- Performance management, in particular project governance and control, operational metrics and management reporting.
I have in mind a tag line for the business being:
"Helping business to discover sustainable value."
I am looking for a letterhead design which utilises my new logo on report templates (powerpoint and word), and letterhead.
Lexiborn defines a mother lode as follows:
"Mother lode is a principal vein or zone of veins of gold or silver ore. The term probably came from a literal translation of the Spanish veta madre, a term common in old Mexican mining. Veta madre, for instance, is the name given to an 11-kilometre-long (6.8 mi) silver vein discovered in 1548 in Guanajuato, New Spain (modern-day Mexico)."
My preference is for black and gold. Logo files are attached in .eps format. All fonts are outlined. The fonts that are used are "Crimson Text" and "Josefin Sans". They are free open source fonts and they are available here: http://www.glyphbarn.com/fonts
Target Market(s)
Medium to large corporates.
Industry/Entity Type
Boutique
Other font styles liked:
- All fonts are outlined. The fonts that are used are "Crimson Text" and "Josefin Sans". They are free open source fonts and they are available here: http://www.glyphbarn.com/fonts

```html
<!DOCTYPE html>
<html lang="en">
<head>
<meta charset="utf-8">
<title>Quillfern Consulting — Letterhead</title>
<link href="https://fonts.googleapis.com/css2?family=Crimson+Text:wght@400;600;700&family=Josefin+Sans:wght@300;400&display=swap" rel="stylesheet">
<style>
  :root {
    --ink: #0b0b0b;
    --gold: #dca926;
    --paper: #ffffff;
    --backdrop: #e4e4e4;
    --faint: #f0f0f0;
  }
  html, body {
    margin: 0;
    padding: 0;
    width: 1000px;
    height: 1200px;
    overflow: hidden;
    background: var(--backdrop);
  }
  .letterhead {
    position: absolute;
    left: 182px;
    top: 137px;
    width: 648px;
    height: 915px;
    background: var(--paper);
    overflow: hidden;
  }
  .brand {
    position: absolute;
    left: 160px;
    top: 33px;
    display: flex;
    align-items: center;
    gap: 14px;
  }
  .brand-square {
    width: 69px;
    height: 69px;
    background: var(--ink);
    flex: none;
  }
  .brand-name {
    font-family: "Crimson Text", serif;
    font-weight: 400;
    font-size: 31px;
    line-height: 1.05;
    color: var(--ink);
    letter-spacing: 0.5px;
    text-transform: uppercase;
    margin: 0;
  }
  .brand-name span { display: block; }
  .backdrop-name {
    position: absolute;
    left: 0;
    right: 0;
    top: 370px;
    text-align: center;
    font-family: "Crimson Text", serif;
    font-weight: 400;
    font-size: 96px;
    line-height: 1;
    color: var(--faint);
    text-transform: uppercase;
    letter-spacing: 2px;
    margin: 0;
  }
  .footer {
    position: absolute;
    left: 0;
    bottom: 0;
    width: 648px;
    height: 70px;
  }
  .footer-wave {
    position: absolute;
    inset: 0;
  }
  .footer-details {
    position: absolute;
    left: 0;
    right: 0;
    top: 29px;
    font-family: "Crimson Text", serif;
    font-weight: 700;
    font-size: 8px;
    color: var(--paper);
    text-align: center;
  }
  .footer-row {
    display: flex;
    justify-content: center;
    align-items: center;
    gap: 6px;
    height: 14px;
    padding-left: 42px;
  }
  .footer-row + .footer-row { margin-top: 4px; }
  .contact-item {
    display: inline-flex;
    align-items: center;
    gap: 9px;
    margin: 0 9px;
  }
  .contact-item.web { letter-spacing: 1px; }
  .icon { width: 13px; height: 12px; flex: none; }
</style>
</head>
<body>
  <main class="letterhead">
    <header class="brand">
      <div class="brand-square"></div>
      <h1 class="brand-name"><span>Quillfern</span><span>Consulting</span></h1>
    </header>

    <p class="backdrop-name" aria-hidden="true">Quillfern</p>

    <footer class="footer">
      <svg class="footer-wave" viewBox="0 0 648 70" preserveAspectRatio="none" aria-hidden="true">
        <path d="M0 5 C120 -1 260 8 380 12 C480 15 580 10 648 6 L648 16 C580 20 480 23 380 21 C260 19 120 12 0 16 Z" fill="var(--gold)"/>
        <path d="M0 24 C140 18 260 24 380 26 C480 28 580 24 648 20 L648 70 L0 70 Z" fill="var(--ink)"/>
      </svg>
      <div class="footer-details">
        <div class="footer-row">
          <svg class="icon" viewBox="0 0 13 12" aria-hidden="true">
            <path d="M6.5 0.5 L12.5 6 L10.5 6 L10.5 11.5 L2.5 11.5 L2.5 6 L0.5 6 Z" fill="var(--paper)"/>
          </svg>
          <span>Level 27, 48 Ashgrove Street, Melbourne VIC 3000, AUSTRALIA</span>
        </div>
        <div class="footer-row">
          <span class="contact-item">
            <svg class="icon" viewBox="0 0 13 12" aria-hidden="true">
              <path d="M0.5 4 C3 1 10 1 12.5 4 L11 5.5 L9 4.5 L9 3.5 C7 3 6 3 4 3.5 L4 4.5 L2 5.5 Z" fill="var(--paper)"/>
              <path d="M3 6.5 L10 6.5 L11.5 11 L1.5 11 Z" fill="var(--paper)"/>
            </svg>
            +61 3 9000 4172
          </span>
          <span class="contact-item">
            <svg class="icon" viewBox="0 0 13 12" aria-hidden="true">
              <rect x="3.5" y="0.5" width="6" height="4" fill="none" stroke="var(--paper)" stroke-width="1"/>
              <rect x="0.5" y="4.5" width="12" height="7" rx="1" fill="var(--paper)"/>
              <rect x="2" y="6" width="2" height="4.5" fill="var(--ink)"/>
            </svg>
            +61 3 9000 4178
          </span>
          <span class="contact-item web">
            <svg class="icon" viewBox="0 0 13 12" aria-hidden="true">
              <circle cx="6.5" cy="6" r="5.2" fill="none" stroke="var(--paper)" stroke-width="1.1"/>
              <ellipse cx="6.5" cy="6" rx="2.2" ry="5.2" fill="none" stroke="var(--paper)" stroke-width="1"/>
              <path d="M1.3 6 H11.7 M2 3.3 H11 M2 8.7 H11" stroke="var(--paper)" stroke-width="0.9"/>
            </svg>
            quillfernconsulting.com.au
          </span>
        </div>
      </div>
    </footer>
  </main>
</body>
</html>
```